Business Card Design

WE are looking for a premium quality Business Cards for a Law Firm . Copies of our current business card is attached.
Updates

Went on vacation/holiday

Contact Information for Business Card

xyz

```html
<!DOCTYPE html>
<html lang="en">
<head>
<meta charset="utf-8">
<title>Marlow Legal – Business Card</title>
<link href="https://fonts.googleapis.com/css2?family=Arimo:wght@400;700&display=swap" rel="stylesheet">
<style>
  :root {
    --bg: #151515;
    --card: #2a2a2a;
    --card-dark: #232323;
    --gold: #c9994a;
    --white: #ffffff;
    --soft: #e6e6e6;
  }
  * { margin: 0; padding: 0; box-sizing: border-box; }
  html, body {
    width: 1200px; height: 963px; overflow: hidden;
    background: var(--bg);
    font-family: "Arimo", Arial, sans-serif;
  }
  .card {
    position: absolute; left: 150px; top: 206px;
    width: 900px; height: 550px;
    border-radius: 34px;
    background: linear-gradient(135deg, var(--card) 0%, var(--card-dark) 100%);
    border: 3px solid var(--gold);
    color: var(--white);
  }
  .identity { position: absolute; left: 78px; top: 128px; }
  .name {
    color: var(--gold); font-weight: 700; font-size: 30px;
    letter-spacing: 0.5px; text-transform: uppercase;
  }
  .role { font-size: 19px; margin-top: 10px; letter-spacing: 0.3px; }
  .credentials { font-size: 19px; margin-top: 6px; }
  .brand {
    position: absolute; right: 78px; top: 66px;
    display: flex; flex-direction: column; align-items: flex-end; gap: 14px;
  }
  .brand-dot {
    width: 82px; height: 82px; border-radius: 50%;
    border: 4px solid var(--gold);
    margin-right: 22px;
  }
  .brand-name {
    font-size: 40px; font-weight: 700; color: var(--white);
    letter-spacing: 1px; text-transform: uppercase; line-height: 1;
  }
  .rule {
    position: absolute; left: 78px; right: 78px; top: 262px;
    height: 2px; background: var(--gold);
  }
  .contacts { position: absolute; left: 78px; top: 292px; list-style: none; }
  .contacts li {
    display: flex; align-items: center; gap: 14px;
    font-size: 20px; height: 36px;
  }
  .contacts svg { width: 20px; height: 20px; flex: none; }
  .address {
    position: absolute; right: 78px; top: 400px;
    font-size: 20px; line-height: 34px; color: var(--soft);
    font-style: normal;
  }
</style>
</head>
<body>
  <main class="card">
    <div class="identity">
      <h1 class="name">Daniel Reyes</h1>
      <p class="role">DIRECTOR &amp; PRINCIPAL SOLICITOR</p>
      <p class="credentials">MBA, Juris Doctor</p>
    </div>

    <div class="brand">
      <span class="brand-dot"></span>
      <span class="brand-name">Marlow Legal</span>
    </div>

    <div class="rule"></div>

    <ul class="contacts">
      <li>
        <svg viewBox="0 0 20 20" fill="none" stroke="var(--gold)" stroke-width="1.8"><path d="M4 2h4l1.5 4-2.5 1.5a10 10 0 0 0 5.5 5.5L14 10.5l4 1.5v4a2 2 0 0 1-2 2A16 16 0 0 1 2 4a2 2 0 0 1 2-2z"/></svg>
        +61 7 3000 1234
      </li>
      <li>
        <svg viewBox="0 0 20 20" fill="none" stroke="var(--gold)" stroke-width="1.8"><rect x="5" y="1.5" width="10" height="17" rx="2"/><line x1="9" y1="15.5" x2="11" y2="15.5"/></svg>
        +61 0400 000 111
      </li>
      <li>
        <svg viewBox="0 0 20 20" fill="none" stroke="var(--gold)" stroke-width="1.8"><rect x="1.5" y="4" width="17" height="12" rx="1"/><path d="M2 5l8 6 8-6"/></svg>
        daniel@marlowlegal.com.au
      </li>
      <li>
        <svg viewBox="0 0 20 20" fill="none" stroke="var(--gold)" stroke-width="1.6"><circle cx="10" cy="10" r="8"/><ellipse cx="10" cy="10" rx="3.5" ry="8"/><line x1="2" y1="10" x2="18" y2="10"/><path d="M3.5 5.5h13M3.5 14.5h13"/></svg>
        www.marlowlegal.com.au
      </li>
    </ul>

    <address class="address">
      Level 2, Harbour House<br>
      48 Kent Street,<br>
      Milton, QLD 4064
    </address>
  </main>
</body>
</html>
```